Northfield Builders Guild Business card

We are looking for a new business card design with photo included.
Our business is a nonprofit construction contractor membership organization. We offer business education, assist with business setup and licensing, provide safety training, and provide a member directory.
URL: www.brickwayguildnetwork.org
Color code:
CMYK: 0 cyan, 42 magenta, 100 yellow, 0 black for Print.
Hexidecimal: #FF9900
RGB: R 255; G 153; B 0

```html
<!DOCTYPE html>
<html lang="en">
<head>
<meta charset="utf-8">
<title>Northfield Builders Guild – Business Card</title>
<link rel="stylesheet" href="https://fonts.googleapis.com/css2?family=Montserrat:wght@800&family=Poppins:wght@400&display=swap">
<style>
  :root {
    --bg: #2b2b2b;
    --orange: #f7981f;
    --ink: #1e1e1e;
    --panel: #333333;
    --paper: #ffffff;
    --light: #f2f2f2;
    --rule: #d9d9d9;
  }
  * { box-sizing: border-box; margin: 0; padding: 0; }
  html, body { width: 1200px; height: 900px; overflow: hidden; }
  body {
    background: var(--bg);
    position: relative;
    font-family: "Poppins", sans-serif;
  }
  .card {
    position: absolute;
    left: 270px;
    width: 660px;
    height: 377px;
    box-shadow: 0 10px 28px rgba(0,0,0,.45);
    overflow: hidden;
  }
  .card-front { top: 50px; background: var(--orange); display: flex; align-items: center; justify-content: center; }
  .card-back { top: 473px; background: var(--paper); display: flex; }

  .brand-name {
    font-family: "Montserrat", sans-serif;
    font-weight: 800;
    color: var(--ink);
    text-transform: uppercase;
    line-height: 1.05;
    letter-spacing: -0.5px;
  }
  .card-front .brand-name { font-size: 38px; text-align: center; }

  .back-brand {
    width: 47%;
    display: flex;
    align-items: center;
    justify-content: center;
    padding: 0 30px;
  }
  .back-brand .brand-name { font-size: 34px; }

  .contact-panel {
    width: 53%;
    background: var(--panel);
    padding: 58px 34px 0 28px;
    color: var(--light);
  }
  .contact-row {
    display: flex;
    align-items: center;
    gap: 16px;
    padding: 12px 0;
    border-bottom: 1px solid var(--rule);
    font-size: 13.5px;
    line-height: 1.45;
  }
  .contact-row:last-child { border-bottom: none; }
  .contact-icon {
    flex: 0 0 44px;
    width: 44px;
    height: 44px;
    border-radius: 50%;
    border: 2px solid var(--light);
    display: flex;
    align-items: center;
    justify-content: center;
  }
  .contact-icon svg { width: 34px; height: 34px; }
</style>
</head>
<body>
  <section class="card card-front">
    <h1 class="brand-name">Northfield<br>Builders Guild</h1>
  </section>

  <section class="card card-back">
    <div class="back-brand">
      <p class="brand-name">Northfield<br>Builders<br>Guild</p>
    </div>
    <div class="contact-panel">
      <div class="contact-row">
        <span class="contact-icon">
          <svg viewBox="0 0 34 34" aria-hidden="true">
            <circle cx="17" cy="17" r="17" fill="var(--orange)"/>
            <path d="M12 10c1-1 2-1 3 0l1.5 2.5c.4.8.2 1.5-.5 2l-1 .8c.8 1.8 2 3 3.7 3.7l.8-1c.5-.7 1.2-.9 2-.5L24 19c1 1 1 2 0 3l-1 1c-4 1-12-7-11-11z" fill="none" stroke="#fff" stroke-width="1.5"/>
          </svg>
        </span>
        <p>P: (555) 318-2047<br>F: 555.204.7731</p>
      </div>
      <div class="contact-row">
        <span class="contact-icon">
          <svg viewBox="0 0 34 34" aria-hidden="true">
            <circle cx="17" cy="17" r="17" fill="var(--orange)"/>
            <g fill="none" stroke="#fff" stroke-width="1.4">
              <circle cx="17" cy="17" r="8"/>
              <ellipse cx="17" cy="17" rx="3.5" ry="8"/>
              <path d="M9 17h16M10.5 13h13M10.5 21h13"/>
            </g>
          </svg>
        </span>
        <p>hello@nbguild.com<br>brickwayguildnetwork.org</p>
      </div>
      <div class="contact-row">
        <span class="contact-icon">
          <svg viewBox="0 0 34 34" aria-hidden="true">
            <circle cx="17" cy="17" r="17" fill="var(--orange)"/>
            <path d="M17 26s-6-6.5-6-11a6 6 0 0 1 12 0c0 4.5-6 11-6 11z" fill="#fff"/>
            <circle cx="17" cy="15" r="2.2" fill="var(--orange)"/>
          </svg>
        </span>
        <p>2400 Ridgeline Ave.<br>Suite #210, Fairview, OR 97000</p>
      </div>
    </div>
  </section>
</body>
</html>
```